Kitchen Tools Infographic - Helpful Items for Healthy Home Meals

We are a weight loss company that provides holistic, natural nutrition programs to consumers -- you can see our web site at www.FernQuill.com. We need a simple infographic to be shared on social media and via email. The topic for the infographic is "Equip Your Kitchen for Healthy Home Meals". We've outlined 5 groups of kitchen tools that are helpful for consumers to have for preparing home meals, and included some framing statistics emphasizing the weight management benefits of preparing meals versus eating out.

Target Market(s)

Women age 35-55

Industry/Entity Type

Health And Wellness

Font styles to use
Sans Serif

Colors
0292cd
9bcb3b

Requirements
Must have
• - FernQuill Logo
• - Graphics summarizing statistic (weight gain)
• - Graphics showing groupings of kitchen tools
Should not have
• body scale graphics
• before/after graphics

```html
<!DOCTYPE html>
<html lang="en">
<head>
<meta charset="utf-8">
<title>Equip Your Kitchen For Healthy Home Meals — FernQuill</title>
<link href="https://fonts.googleapis.com/css2?family=Montserrat:wght@400;500;700;800;900&family=Raleway:wght@400;500&display=swap" rel="stylesheet">
<style>
:root{
  --blue:#0292cd;
  --green:#9bcb3b;
  --slate:#37474f;
  --ink:#3a3a3a;
  --panel:#e4e6e8;
  --band:#d7dde2;
  --sky:#cfeaf6;
  --footer:#333436;
  --gold:#f4c20d;
}
*{margin:0;padding:0;box-sizing:border-box}
html,body{width:1200px;height:1200px;overflow:hidden;background:#fff}
.stage{width:1200px;height:1200px;position:relative;display:flex;justify-content:center}
.sheet{width:572px;height:1376px;position:absolute;top:0;left:50%;margin-left:-286px;transform:scale(.872);transform-origin:top center;background:#fff;font-family:"Raleway",sans-serif;color:var(--ink);overflow:hidden}
.abs{position:absolute}
.hero-photo{left:0;top:0;width:572px;height:340px}
.hero-title{left:44px;top:50px;font-family:"Montserrat",sans-serif;font-weight:800;font-size:44px;line-height:47px;color:#fff}
.hero-title .accent{color:var(--green)}
.why-title{left:0;width:572px;top:352px;text-align:center;font-family:"Montserrat",sans-serif;font-weight:500;font-size:43px;color:var(--blue)}
.why-copy{left:20px;width:532px;top:404px;text-align:center;font-size:14px;line-height:21px;color:#444}
.chart-title{font-family:"Montserrat",sans-serif;font-weight:700;font-size:14px;line-height:18px;text-align:center}
.chart-title.blue{color:var(--blue)}
.chart-title.green{color:var(--green)}
.charts{left:0;top:470px;width:572px;height:140px}
.panel{left:25px;top:625px;width:532px;height:655px;background:var(--panel)}
.sky-stripe{left:530px;top:635px;width:24px;height:645px;background:var(--sky)}
.band{position:absolute;height:84px;background:var(--band)}
.badge{position:absolute;width:108px;height:108px;border-radius:50%;border:7px solid var(--slate);display:flex;flex-direction:column;align-items:center;justify-content:center;font-family:"Montserrat",sans-serif;font-weight:500;color:#fff;font-size:25px;line-height:27px;text-align:center}
.badge.blue{background:var(--blue)}
.badge.green{background:var(--green)}
.tool{position:absolute;font-size:10px;line-height:13px;color:#555;width:98px}
.tool b{display:block;font-weight:500;color:#333}
.icon{position:absolute;border-radius:6px}
.icon.slate{background:#5b6b75}
.icon.blue{background:var(--blue)}
.icon.green{background:#8dbb3a}
.icon.red{background:#d9433b}
.icon.light{background:#c9ccce}
.closing{left:0;width:572px;top:1204px;text-align:center;font-size:14px;line-height:21px;color:#333}
.cta{left:236px;top:1250px;width:100px;height:22px;border-radius:11px;background:var(--blue);border:2px solid #fff;box-shadow:0 0 0 1px var(--blue);color:#fff;font-family:"Montserrat",sans-serif;font-weight:800;font-size:11px;letter-spacing:1px;text-align:center;line-height:18px}
.footer{left:0;top:1282px;width:572px;height:94px;background:var(--footer)}
.brand{left:0;width:572px;top:1290px;display:flex;align-items:center;justify-content:center;gap:10px}
.brand-dot{width:26px;height:26px;border-radius:50%;background:var(--green)}
.brand-name{font-family:"Montserrat",sans-serif;font-weight:500;font-size:28px;color:var(--blue)}
.url{left:0;width:572px;top:1330px;text-align:center;font-size:14px;color:var(--blue)}
.sources{left:0;width:572px;top:1352px;text-align:center;font-size:6.5px;line-height:9px;color:#ddd}
.sources em{font-style:normal;color:var(--gold);font-weight:500}
</style>
</head>
<body>
<div class="stage">
<main class="sheet">

  <svg class="abs hero-photo" viewBox="0 0 572 340" role="img" aria-label="Photo of a warm home kitchen with wooden shelves and a white stove">
    <defs>
      <linearGradient id="heroGrad" x1="0" y1="0" x2="1" y2="0">
        <stop offset="0" stop-color="#1c1c3a"/>
        <stop offset=".55" stop-color="#2a2440"/>
        <stop offset=".8" stop-color="#6b4124"/>
        <stop offset="1" stop-color="#8a5a34"/>
      </linearGradient>
    </defs>
    <path d="M0 0H572V230C520 270 470 300 400 292C320 282 260 262 190 282C120 304 60 330 0 300Z" fill="url(#heroGrad)"/>
  </svg>
  <h1 class="abs hero-title">Equip<br><span class="accent">Your Kitchen</span><br>For Healthy<br><span class="accent">Home Meals</span></h1>

  <h2 class="abs why-title">Why Cook at Home?</h2>
  <p class="abs why-copy">Those who eat out consume an average of 134 calories more per meal. Americans eat out an average of 4.5 times per week, so those extra calories can add up to substantial weight gain -- and give you a reason to prepare your</p>

  <svg class="abs charts" viewBox="0 0 572 140" font-family="Raleway, sans-serif">
    <!-- excess calories chart -->
    <line x1="10" y1="12" x2="10" y2="100" stroke="#8dbb3a" stroke-width="2"/>
    <line x1="10" y1="97" x2="296" y2="97" stroke="#8dbb3a" stroke-width="2"/>
    <g fill="#8dbb3a"><circle cx="52" cy="97" r="3"/><circle cx="91" cy="97" r="3"/><circle cx="130" cy="97" r="3"/><circle cx="169" cy="97" r="3"/><circle cx="208" cy="97" r="3"/><circle cx="247" cy="97" r="3"/><circle cx="286" cy="97" r="3"/></g>
    <g fill="var(--blue)" font-size="9.5" text-anchor="middle"><text x="52" y="116">100</text><text x="91" y="116">200</text><text x="130" y="116">300</text><text x="169" y="116">400</text><text x="208" y="116">500</text><text x="247" y="116">600</text><text x="286" y="116">700</text></g>
    <text x="22" y="44" font-size="10" fill="var(--blue)">Calories per week</text>
    <line x1="12" y1="51" x2="248" y2="51" stroke="var(--blue)" stroke-width="3"/>
    <circle cx="248" cy="51" r="4" fill="var(--blue)"/>
    <text x="22" y="69" font-size="10" fill="#8dbb3a">Calories per  meal</text>
    <line x1="12" y1="78" x2="68" y2="78" stroke="#8dbb3a" stroke-width="3"/>
    <circle cx="68" cy="78" r="4" fill="#8dbb3a"/>
    <!-- pounds gained chart -->
    <line x1="336" y1="20" x2="336" y2="108" stroke="#aaa" stroke-width="1"/>
    <g stroke="#ddd"><line x1="340" y1="38" x2="535" y2="38"/><line x1="340" y1="52" x2="535" y2="52"/><line x1="340" y1="66" x2="535" y2="66"/><line x1="340" y1="80" x2="535" y2="80"/><line x1="340" y1="94" x2="535" y2="94"/><line x1="340" y1="107" x2="535" y2="107"/></g>
    <g font-size="9" fill="#444" text-anchor="end"><text x="325" y="111">2</text><text x="325" y="97">4</text><text x="325" y="83">6</text><text x="325" y="69">8</text><text x="325" y="55">10</text></g>
    <g font-size="9" fill="var(--blue)" text-anchor="middle"><text x="355" y="122">2</text><text x="379" y="122">4</text><text x="402" y="122">6</text><text x="426" y="122">8</text><text x="449" y="122">10</text><text x="472" y="122">12</text></g>
    <text x="494" y="122" font-size="13" font-family="Montserrat, sans-serif" font-weight="500" fill="var(--blue)">MONTHS</text>
    <g fill="var(--blue)"><rect x="350" y="97" width="10" height="11"/><rect x="397" y="76" width="10" height="32"/><rect x="468" y="45" width="10" height="63"/></g>
  </svg>
  <div class="abs chart-title blue" style="left:40px;top:466px;width:230px">Excess Calories<br>from Restaurant Meals</div>
  <div class="abs chart-title green" style="left:330px;top:471px;width:230px">Pounds Gained<br>from Restaurant Meals</div>

  <div class="abs panel"></div>
  <div class="abs sky-stripe"></div>

  <svg class="abs" style="left:0;top:620px" width="572" height="660" viewBox="0 0 572 660" fill="none" stroke="var(--slate)" stroke-width="5">
    <path d="M285 5V32H500"/>
    <path d="M500 134H60"/>
    <path d="M60 240H500"/>
    <path d="M500 344H60"/>
    <path d="M60 448H500"/>
    <path d="M285 550V578"/>
  </svg>

  <div class="band" style="left:25px;top:655px;width:470px"></div>
  <div class="band" style="left:70px;top:757px;width:490px"></div>
  <div class="band" style="left:25px;top:862px;width:470px"></div>
  <div class="band" style="left:70px;top:966px;width:490px"></div>
  <div class="band" style="left:25px;top:1070px;width:470px"></div>

  <!-- PREP -->
  <div class="tool" style="left:25px;top:670px;width:80px"><b>Cutting Board</b>Essential for prepping meat and vegetables</div>
  <div class="icon green" role="img" aria-label="Cutting board with vegetables" style="left:100px;top:670px;width:28px;height:56px"></div>
  <div class="tool" style="left:147px;top:667px"><b>Chef's Knife</b>Go for quality to make chopping, dicing and slicing faster and easier</div>
  <div class="icon slate" role="img" aria-label="Knife block" style="left:232px;top:668px;width:30px;height:56px"></div>
  <div class="tool" style="left:290px;top:669px;width:95px"><b>Digital Food Scale</b>Get the precision you need for perfect recipes and portion control</div>
  <div class="icon slate" role="img" aria-label="Digital food scale" style="left:390px;top:688px;width:44px;height:36px"></div>
  <div class="badge blue" style="left:446px;top:651px">1.<br>PREP:</div>

  <!-- TECH -->
  <div class="badge green" style="left:8px;top:752px">2.<br>TECH</div>
  <div class="icon red" role="img" aria-label="High-powered blender" style="left:128px;top:780px;width:30px;height:50px"></div>
  <div class="tool" style="left:165px;top:765px;width:80px"><b>High-Powered Blender</b>Make highly nutritious, healthy drinks from fruits and veggies</div>
  <div class="icon slate" role="img" aria-label="Slow cooker" style="left:258px;top:785px;width:42px;height:40px"></div>
  <div class="tool" style="left:306px;top:781px;width:80px"><b>Slow Cooker</b>Cook delicious meals while you are at work</div>
  <div class="icon slate" role="img" aria-label="Pressure cooker" style="left:410px;top:781px;width:40px;height:44px"></div>
  <div class="tool" style="left:462px;top:780px;width:88px"><b>Pressure Cooker</b>Create single pot meals in 20 minutes or less</div>

  <!-- COOK -->
  <div class="tool" style="left:30px;top:883px;width:90px"><b>Ceramic Pan</b>Nonstick cooking surface allows you to cook without oil</div>
  <div class="icon slate" role="img" aria-label="Ceramic frying pan" style="left:114px;top:875px;width:42px;height:60px;border-radius:21px"></div>
  <div class="tool" style="left:170px;top:885px;width:92px"><b>Vegetable Steamer</b>Preserve nutrients and natural, fresh taste</div>
  <div class="icon light" role="img" aria-label="Vegetable steamer" style="left:266px;top:882px;width:44px;height:46px"></div>
  <div class="tool" style="left:320px;top:876px;width:82px"><b>Baking Sheet</b>Ideal for roasting vegetables in the oven or baking chicken and fish dishes</div>
  <div class="icon light" role="img" aria-label="Baking sheet" style="left:404px;top:876px;width:34px;height:54px"></div>
  <div class="badge blue" style="left:446px;top:858px">3.<br>COOK</div>

  <!-- SERVE -->
  <div class="badge green" style="left:8px;top:962px">4.<br>SERVE</div>
  <div class="icon red" role="img" aria-label="Cloth napkins" style="left:128px;top:985px;width:40px;height:42px"></div>
  <div class="tool" style="left:174px;top:983px;width:74px"><b>Cloth Napkins</b>To reduce waste and dress up your table</div>
  <div class="icon blue" role="img" aria-label="Dinnerware plate" style="left:252px;top:985px;width:38px;height:48px;border-radius:14px"></div>
  <div class="tool" style="left:308px;top:978px;width:80px"><b>Dinnerware</b>Pre-plate meals rather than serving family style to control portions</div>
  <div class="icon blue" role="img" aria-label="Small plates" style="left:402px;top:978px;width:42px;height:50px;border-radius:14px"></div>
  <div class="tool" style="left:452px;top:976px;width:96px"><b>Small Plates</b>Use salad plates and smaller dishware to manage perception of food volume</div>

  <!-- STORE -->
  <div class="tool" style="left:28px;top:1078px;width:94px"><b>Glass Storage Containers</b>Keep your healthy leftovers so nothing goes to waste</div>
  <div class="icon light" role="img" aria-label="Glass storage container" style="left:124px;top:1090px;width:64px;height:32px"></div>
  <div class="tool" style="left:196px;top:1078px;width:80px"><b>Mason Jars</b>Perfect for premade salads that you can bring to work</div>
  <div class="icon light" role="img" aria-label="Mason jar" style="left:276px;top:1090px;width:32px;height:44px"></div>
  <div class="tool" style="left:320px;top:1078px;width:98px"><b>Freezer Safe Re-Sealable Bags</b>Prepare double batches to make the most of your time</div>
  <div class="icon light" role="img" aria-label="Freezer bag" style="left:420px;top:1090px;width:30px;height:40px"></div>
  <div class="badge blue" style="left:446px;top:1066px">5.<br>STORE</div>

  <p class="abs closing">FernQuill can help you develop healthier eating habits.<br>We invite you to learn more.</p>
  <div class="abs cta">CONTACT US</div>

  <footer class="abs footer"></footer>
  <div class="abs brand"><span class="brand-dot"></span><span class="brand-name">FERNQUILL</span></div>
  <div class="abs url">www.FernQuill.com</div>
  <div class="abs sources"><em>Sources:</em> https://www.foodstatsdesk.org/eating-out-data/2010/june/eating-out-increases-daily-calorie-intake <em>and</em><br>https://www.diningpulse.com/b/the-state-of-american-dining-in-2016</div>

</main>
</div>
</body>
</html>
```